Visit card

Industry/Entity Type

Health Care

Contact Information for Business Card

O VITALE SYSTEMES
Odile Ferrandi - chef de Projet

Requirements
Must have
• 318 Hector Delaunay Street 58210 BÉTHUNE Tel: 33 (0) 387 419 264 Mobile: 06 42 93 17 58 Web: www.vobelasystems.example Contact: o.ferrandi@o-vitalesystemes.example
Should not have
• Respect for color

```html
<!DOCTYPE html>
<html lang="fr">
<head>
<meta charset="utf-8">
<title>O Vitale Systemes – carte de visite</title>
<link href="https://fonts.googleapis.com/css2?family=Barlow:wght@400;500;600;700&display=swap" rel="stylesheet">
<style>
  :root {
    --backdrop: #aeb9bd;
    --card: #ffffff;
    --red: #ec1f2b;
    --red-deep: #c1191f;
    --ink: #1a1a1a;
    --graphite: #4a4a4a;
  }
  * { margin: 0; padding: 0; box-sizing: border-box; }
  html, body {
    width: 1200px; height: 1000px; overflow: hidden;
    background: var(--backdrop);
    font-family: "Barlow", Arial, sans-serif;
  }
  .canvas { position: relative; width: 1200px; height: 1000px; }
  .card {
    position: absolute; left: 343px; width: 515px; height: 333px;
    background: var(--card); overflow: hidden;
  }
  .card--front { top: 140px; }
  .card--back { top: 527px; }

  /* Front */
  .brand {
    position: absolute; left: 49px; top: 106px;
    display: flex; align-items: center; gap: 34px;
  }
  .brand__dot {
    width: 120px; height: 120px; border-radius: 50%;
    background: var(--graphite); flex: none;
  }
  .brand__name {
    color: var(--red); font-weight: 600; line-height: 1;
  }
  .brand__line1 { display: block; font-size: 48px; letter-spacing: 1px; }
  .brand__line2 { display: block; font-size: 23px; letter-spacing: 5px; margin-top: 8px; }

  /* Back */
  .back-art { position: absolute; inset: 0; }
  .back-brand {
    position: absolute; right: 22px; top: 48px;
    color: #fff; font-weight: 600; font-size: 12px; letter-spacing: 0.5px;
  }
  .holder { position: absolute; left: 23px; top: 139px; color: var(--ink); }
  .holder__name { font-size: 18px; font-weight: 700; line-height: 1.2; }
  .holder__role { font-size: 15px; font-weight: 400; margin-top: 6px; }
  .contacts {
    position: absolute; left: 23px; top: 213px; list-style: none;
    color: var(--ink); font-size: 13.5px;
  }
  .contacts li { display: flex; align-items: center; height: 26px; }
  .contacts svg { width: 10px; height: 10px; margin-right: 9px; flex: none; fill: var(--ink); }
</style>
</head>
<body>
<main class="canvas">
  <section class="card card--front">
    <div class="brand">
      <span class="brand__dot"></span>
      <span class="brand__name">
        <span class="brand__line1">O VITALE</span>
        <span class="brand__line2">SYSTEMES</span>
      </span>
    </div>
  </section>

  <section class="card card--back">
    <svg class="back-art" viewBox="0 0 515 333" width="515" height="333" aria-hidden="true">
      <rect width="515" height="333" fill="var(--red-deep)"/>
      <polygon points="0,0 515,0 0,122" fill="var(--red)"/>
      <path d="M0,122 C150,86 430,120 515,333 L0,333 Z" fill="var(--card)"/>
    </svg>
    <span class="back-brand">O VITALE SYSTEMES</span>

    <div class="holder">
      <p class="holder__name">Odile Ferrandi</p>
      <p class="holder__role">chef de Projet</p>
    </div>

    <ul class="contacts">
      <li><svg viewBox="0 0 10 10"><path d="M5 0a3.5 3.5 0 0 0-3.5 3.5C1.5 6 5 10 5 10s3.5-4 3.5-6.5A3.5 3.5 0 0 0 5 0zm0 5a1.4 1.4 0 1 1 0-2.8A1.4 1.4 0 0 1 5 5z"/></svg>318 Hector Delaunay Street 58210 Béthune</li>
      <li><svg viewBox="0 0 10 10"><path d="M2 0.5l1.6 2.2-1 1.1c.6 1.3 1.6 2.3 2.9 2.9l1.1-1L9 7.3 8 9.3C4 9 1 6 .7 2z"/></svg>+33 (0) 387 419 264 / 06 42 93 17 58</li>
      <li><svg viewBox="0 0 10 10"><circle cx="5" cy="5" r="4.3" fill="none" stroke="#1a1a1a" stroke-width="1.1"/><path d="M.7 5h8.6M5 .7c-2.2 2.4-2.2 6.2 0 8.6M5 .7c2.2 2.4 2.2 6.2 0 8.6" fill="none" stroke="#1a1a1a" stroke-width="0.9"/></svg>www.vobelasystems.example</li>
      <li><svg viewBox="0 0 10 10"><path d="M0 2h10v6H0z"/><path d="M0 2l5 3.4L10 2" fill="none" stroke="#fff" stroke-width="0.9"/></svg>o.ferrandi@o-vitalesystemes.example</li>
    </ul>
  </section>
</main>
</body>
</html>
```